Stylish Business Card for Modern hair salon

I need a simple business card design using our salon logo and colours that are in the logo. We service clients of all ages but predominantly those in the 18 to 55 age range. We have a young staff and are looking to have a card that will present a modern and clean image that represents who we are. The card should be in black and white same as our logo. Minimal use of other colours is allowed.

Industry/Entity Type

Hair And Beauty

Contact Information for Business Card

The design should have the following information
salon name - TR Hair Studio
address - 2751 Birchfield Rd.E. Mississauga, ON L7P3K2
phone - 905 614-2870
website - trhairexample.ca
instagram - tr.hairstudio
twitter - @TR_HairStudio

Colors
000000
ffffff
474747

Requirements
Must have
• simple design, salon name, address, phone, website, instagram, twitter info
• Back of card should have the following:
• YOUR NEXT APPOINTMENT
• DATE
• TIME
Nice to have
• simple design, clear to see and read,
• predominantly black and white colour, minimal use of other colours is ok
Should not have
• many colours, various fonts

```html
<!DOCTYPE html>
<html lang="en">
<head>
<meta charset="utf-8">
<title>TR Hair Studio – Business Card</title>
<link rel="stylesheet" href="https://fonts.googleapis.com/css2?family=Tinos:wght@400;700&display=swap">
<style>
  :root {
    --backdrop: #ebe9ea;
    --card: #fdfdf0;
    --ink: #000000;
    --text: #3a3a3a;
    --charcoal: #474747;
    --shadow: rgba(0,0,0,0.28);
  }
  * { margin: 0; padding: 0; box-sizing: border-box; }
  html, body {
    width: 1200px; height: 1000px; overflow: hidden;
    background: var(--backdrop);
    font-family: "Tinos", "Times New Roman", serif;
    color: var(--text);
  }
  .canvas { position: relative; width: 1200px; height: 1000px; }

  .card {
    position: absolute; left: 251px; width: 676px; height: 385px;
    box-shadow: 8px 9px 6px var(--shadow);
  }
  .card--front { top: 96px; background: var(--card); }
  .card--back { top: 519px; background: var(--charcoal); }

  /* Front */
  .brand-name {
    position: absolute; left: 99px; top: 68px;
    font-size: 46px; font-weight: 700; color: var(--ink);
    letter-spacing: 1px; line-height: 1;
  }
  .web-vertical {
    position: absolute; left: 37px; bottom: 106px;
    writing-mode: vertical-rl; transform: rotate(180deg);
    font-size: 15px; letter-spacing: 2px; white-space: nowrap; line-height: 18px;
  }
  .web-dash {
    position: absolute; left: 44px; top: 296px;
    width: 4px; height: 10px; background: var(--text);
  }
  .studio-block {
    position: absolute; left: 99px; top: 242px;
    border-left: 2px solid var(--ink); padding-left: 22px;
    font-size: 19px; line-height: 22px; color: var(--ink);
    letter-spacing: 0.5px;
  }
  .address {
    position: absolute; left: 370px; top: 97px;
    font-size: 15.5px; line-height: 22px; letter-spacing: 1.2px;
  }
  .contacts {
    position: absolute; left: 370px; top: 236px;
    list-style: none; font-size: 15.5px; letter-spacing: 1.2px;
  }
  .contacts li { display: flex; align-items: center; height: 24px; }
  .contacts svg { width: 16px; height: 16px; margin-right: 17px; flex: none; }

  /* Back */
  .back-face {
    position: absolute; left: 24px; top: 24px; right: 24px; bottom: 24px;
    background: var(--card);
  }
  .appointment-frame {
    position: absolute; left: 82px; top: 44px; width: 464px; height: 249px;
    border: 2px solid var(--charcoal);
  }
  .appointment-title {
    position: absolute; top: 50px; left: 0; right: 0; text-align: center;
    font-size: 20px; letter-spacing: 2.2px; font-weight: 400;
  }
  .appointment-fields {
    position: absolute; left: 45px; top: 119px;
    font-size: 14.5px; letter-spacing: 1.3px; line-height: 27px;
    white-space: nowrap; overflow: hidden; width: 376px;
  }
  .back-web {
    position: absolute; left: 0; right: 0; top: 305px; text-align: center;
    font-size: 14.5px; letter-spacing: 1.3px;
  }
</style>
</head>
<body>
<main class="canvas">
  <section class="card card--front" aria-label="Card front">
    <div class="brand-name">TR Hair</div>
    <div class="web-vertical">www.trhairexample.ca</div>
    <div class="web-dash"></div>
    <div class="studio-block">TR<br>HAIR<br>STUDIO</div>
    <p class="address">2751 Birchfield Rd.E.<br>Mississauga, ON L7P3K2</p>
    <ul class="contacts">
      <li>
        <svg viewBox="0 0 16 16" aria-hidden="true"><rect x="4" y="1" width="8" height="14" rx="1.5" fill="none" stroke="#3a3a3a" stroke-width="1.5"/><line x1="7" y1="12.5" x2="9" y2="12.5" stroke="#3a3a3a" stroke-width="1.2"/></svg>
        905 614-2870
      </li>
      <li>
        <svg viewBox="0 0 16 16" aria-hidden="true"><rect x="2" y="2" width="12" height="12" fill="none" stroke="#3a3a3a" stroke-width="1.6"/></svg>
        tr.hairstudio
      </li>
      <li>
        <svg viewBox="0 0 16 16" aria-hidden="true"><circle cx="8" cy="8" r="6" fill="#3a3a3a"/></svg>
        @TR_HairStudio
      </li>
    </ul>
  </section>

  <section class="card card--back" aria-label="Card back">
    <div class="back-face">
      <div class="appointment-frame">
        <h2 class="appointment-title">YOUR NEXT APPOINTMENT</h2>
        <div class="appointment-fields">
          DATE ..................................................................<br>
          .........................................................................<br>
          TIME ..................................................................
        </div>
      </div>
      <div class="back-web">www.trhairexample.ca</div>
    </div>
  </section>
</main>
</body>
</html>
```